Business Card Design

Velvet Pixel Promotions

An online marketing consulting & strategy business for the cosmetic niche

We specialise in Increasing Leads, Conversions & Content Marketing

I am looking for a very clean, BOLD business card that is simple & effective

Target Market(s)

cosmetic surgeons & cosmetic clinics

Industry/Entity Type

Marketing

Contact Information for Business Card

Darren Okoye
Online Marketing Strategist

Darren@VelvetPixelPromotions.example
0491 268 517

LinkedIn: in/darrenokoye

```html
<!DOCTYPE html>
<html lang="en">
<head>
<meta charset="utf-8">
<title>Velvet Pixel Promotions — Business Card</title>
<link rel="stylesheet" href="https://fonts.googleapis.com/css2?family=Cinzel:wght@600&family=Tinos&family=Courier+Prime&display=swap">
<style>
  :root {
    --backdrop: #d3e8f3;
    --band-deep: #1fa6d2;
    --band-light: #5ccbea;
    --card-white: #ffffff;
    --card-mist: #eef6fa;
    --ink: #3b3d40;
    --ink-soft: #555a5e;
    --accent-green: #8cc63f;
    --accent-cyan: #27a9d6;
    --flourish-a: #6a5cb8;
    --flourish-b: #b9e04a;
  }
  * { box-sizing: border-box; margin: 0; padding: 0; }
  html, body { width: 1200px; height: 741px; overflow: hidden; }
  body { background: var(--backdrop); position: relative; }

  .card {
    position: absolute;
    width: 540px;
    height: 300px;
    background: linear-gradient(180deg, var(--card-white) 0%, var(--card-mist) 100%);
    box-shadow: 0 10px 24px rgba(20, 70, 100, 0.28);
    overflow: hidden;
  }
  .card--front { left: 50px; top: 110px; }
  .card--back  { left: 610px; top: 330px; }

  .band {
    position: absolute; left: 0; right: 0;
    background: linear-gradient(90deg, var(--band-deep), var(--band-light) 70%, var(--band-deep));
  }
  .band--top { top: 0; height: 56px; }
  .band--bottom { bottom: 0; height: 64px; }

  .flourish {
    position: absolute; top: 0; right: 0;
    width: 90px; height: 56px;
    background: linear-gradient(135deg, transparent 20%, var(--flourish-a) 55%, var(--flourish-b) 90%);
    opacity: 0.55;
  }
  .flourish--low {
    top: auto; bottom: 64px; height: 26px; width: 60px;
    background: linear-gradient(160deg, transparent 30%, var(--flourish-b));
  }

  .brand {
    position: absolute;
    display: flex; align-items: center; gap: 12px;
  }
  .brand__dot {
    width: 50px; height: 50px; border-radius: 50%;
    background: var(--accent-green);
    flex: none;
  }
  .brand__name {
    font-family: "Cinzel", serif;
    font-weight: 600;
    font-size: 25px;
    line-height: 25px;
    letter-spacing: 2px;
    color: var(--ink);
  }
  .card--front .brand { left: 135px; top: 92px; }
  .card--back .brand { left: 48px; top: 110px; }
  .card--back .brand__name { font-size: 22px; line-height: 22px; }
  .card--back .brand__dot { width: 44px; height: 44px; }

  .email {
    position: absolute; left: 0; right: 0; top: 200px;
    text-align: center;
    font-family: "Tinos", serif;
    font-size: 14px;
    color: var(--ink);
  }

  .person {
    position: absolute; left: 300px; top: 88px;
  }
  .person__name, .person__role {
    font-family: "Cinzel", serif;
    font-weight: 600;
    font-size: 14px;
    line-height: 24px;
    letter-spacing: 1px;
    color: #111;
  }
  .person__contact {
    margin-top: 22px;
    font-family: "Courier Prime", monospace;
    font-size: 10.5px;
    line-height: 13px;
    color: var(--ink-soft);
  }
</style>
</head>
<body>

  <section class="card card--front" aria-label="Business card front">
    <div class="band band--top"></div>
    <div class="flourish" role="img" aria-label="Decorative colour swirl"></div>
    <div class="brand">
      <span class="brand__dot"></span>
      <p class="brand__name">Velvet<br>Pixel<br>Promotions</p>
    </div>
    <p class="email">Darren@VelvetPixelPromotions.example</p>
    <div class="band band--bottom"></div>
  </section>

  <section class="card card--back" aria-label="Business card back">
    <div class="band band--top"></div>
    <div class="flourish" role="img" aria-label="Decorative colour swirl"></div>
    <div class="brand">
      <span class="brand__dot"></span>
      <p class="brand__name">Velvet<br>Pixel<br>Promotions</p>
    </div>
    <div class="person">
      <p class="person__name">Darren Okoye</p>
      <p class="person__role">Online Marketing<br>Strategist</p>
      <p class="person__contact">c: 0491-268-517<br>LinkedIn:in/darrenokoye</p>
    </div>
    <div class="flourish flourish--low" role="img" aria-label="Decorative colour swirl"></div>
    <div class="band band--bottom"></div>
  </section>

</body>
</html>
```